Veterinary Hospital Brochure - 2 Drafts - 1 Normal and 1 Fun.

Meadowbrook Pet Hospital needs a brochure to promote our veterinary hospital. These will be delivered to local mailboxes. I would like to see atleast 2 submissions from each designer.
One submission conservative and A4 folded DL and another submission more radical and interesting with innovative folding or crazy concepts. Maybe the brochure could be designed to fold into a dog house ?
I want at least one version to be VERY SIMPLE AND INTIMATE.
Our existing website is here: http://furlane.example/ and our new website will look like this: http://trial4.pagemint.example/#home
Please use colors and images from the new website, and information from the old website. The heading font used in the new site is Qorvatype - Otter Tilt Sketchline
I want the brochure to be simple and engaging on first view, and then provide the opportunity to find more information if desired. The brochure needs to be captivating on the outside so people don't throw it away immediately.

We will soon need letterhead, flags, pens, business cards, signs and vouchers so there is the opportunity for more work for the successful designer.

Target Market(s)

Women 25 to 44

Industry/Entity Type

Veterinary

Contact Information for Business Card

Meadowbrook Pet Hospital
14 Marlow Crescent
Tamsworth Vale
NSW 2417
Phone: 02 61938205
Emergency: 0417360592
Fax: 02 83159462
www.meadowbrookvets.example
contact@meadowbrookvets.example

Font styles to use
Script

Requirements
Must have
• Colors from the new website: http://meadowbrookvets.example/ and new logo.
• Information from the old website: http://furlane.example/
• 2 drafts - A normal A4 folded DL flyer and an interesting crazy design.
Nice to have
• VERY SIMPLE
• Subdued
• Intimate
Should not have
• Intense colours
• Red

```html
<!DOCTYPE html>
<html lang="en">
<head>
<meta charset="utf-8">
<title>Meadowbrook Pet Hospital – Tri-fold Brochure</title>
<link href="https://fonts.googleapis.com/css2?family=Open+Sans:wght@400;600;700&display=swap" rel="stylesheet">
<style>
  :root{
    --backdrop:#e4e4e4;
    --peach:#f7e2d2;
    --peach-deep:#efc9a8;
    --brown:#6b5646;
    --mint:#d7ebd3;
    --mint-soft:#eef6ec;
    --green:#8cc63f;
    --orange:#f0883a;
    --ink:#4b3c31;
    --ink-soft:#6f6259;
    --white:#ffffff;
  }
  *{box-sizing:border-box;margin:0;padding:0}
  html,body{width:1200px;height:800px;overflow:hidden}
  body{background:var(--backdrop);font-family:"Open Sans",Arial,sans-serif;color:var(--ink)}
  .brochure{position:absolute;left:60px;top:20px;width:1080px;height:760px;display:flex;box-shadow:0 10px 30px rgba(0,0,0,.18)}
  .panel{position:relative;width:360px;height:760px;overflow:hidden}

  /* Left panel */
  .panel--intro{background:linear-gradient(180deg,var(--peach) 0%,#f9e8db 45%,var(--peach-deep) 100%)}
  .intro-copy{position:absolute;left:40px;top:100px;width:280px;font-size:12.5px;line-height:1.55;color:var(--ink-soft)}
  .intro-copy p{margin-bottom:12px}
  .intro-photo{position:absolute;left:0;right:0;top:420px;bottom:0;
    background:linear-gradient(180deg,rgba(239,201,168,0) 0%,#d8ad87 35%,#b98d6a 75%,#9f7757 100%)}
  .book-badge{position:absolute;left:36px;top:370px;width:288px;height:92px;background:var(--white);border-radius:14px;
    box-shadow:0 2px 6px rgba(0,0,0,.12);text-align:center;padding-top:28px}
  .book-badge__icon{position:absolute;left:50%;top:-20px;transform:translateX(-50%);width:40px;height:40px;border-radius:50%;background:var(--green);border:3px solid var(--white)}
  .book-badge__title{font-size:28px;font-weight:700;color:var(--orange);letter-spacing:1px;line-height:1}
  .book-badge__url{font-size:19px;color:var(--ink-soft);margin-top:4px}
  .intro-phone{position:absolute;left:40px;bottom:34px;color:var(--white);font-size:34px;font-weight:700;display:flex;align-items:center;gap:10px}

  /* Middle panel */
  .panel--contact{background:var(--brown)}
  .contact-photo{position:absolute;inset:0;background:radial-gradient(ellipse at 50% 35%,#8a7767 0%,#6d5848 55%,#5a4738 100%)}
  .hours{position:absolute;left:30px;top:46px;width:300px;height:86px;border:2px solid rgba(255,255,255,.85);border-radius:14px;background:rgba(255,255,255,.12);
    color:var(--white);display:grid;grid-template-columns:76px 1fr;align-content:center;row-gap:4px;padding:14px 0 0 22px}
  .hours__icon{position:absolute;left:50%;top:-18px;transform:translateX(-50%);width:36px;height:36px;border-radius:50%;background:var(--orange);border:2px solid var(--white)}
  .hours__day{font-weight:700;font-size:17px}
  .hours__time{font-size:17px}
  .contact-name{position:absolute;left:0;right:0;top:230px;text-align:center;color:var(--white);font-weight:700;font-size:26px;line-height:1.15}
  .contact-name__dot{display:block;margin:0 auto 12px;width:44px;height:44px;border-radius:50%;background:rgba(255,255,255,.9)}
  .contact-list{position:absolute;left:0;right:0;top:400px;list-style:none;text-align:center;color:var(--white);font-size:13px;line-height:1.45}
  .contact-list li{margin-bottom:16px}
  .contact-list svg{display:block;margin:0 auto 3px}

  /* Right panel */
  .panel--cover{background:linear-gradient(180deg,var(--mint) 0%,var(--mint-soft) 50%,#f4f1ec 100%)}
  .cover-head{position:absolute;left:30px;right:30px;top:70px;display:flex;flex-direction:column;align-items:center;text-align:center}
  .cover-brand__dot{width:52px;height:52px;border-radius:50%;background:var(--green);margin-bottom:14px}
  .cover-brand{color:var(--ink);font-weight:700;font-size:30px;line-height:1.15}
  .cover-tagline{margin-top:16px;font-size:13px;line-height:1.5;color:var(--ink)}
  .services{display:flex;justify-content:space-between;width:100%;margin-top:22px;list-style:none}
  .service{width:70px;text-align:center;font-size:8.5px;line-height:1.2;color:var(--ink-soft);text-transform:uppercase}
  .service__icon{display:block;margin:0 auto 6px;width:44px;height:44px;border-radius:50%;background:var(--green);border:2px solid var(--white);position:relative}
  .service__icon::after{content:"";position:absolute;left:50%;top:50%;width:14px;height:14px;border-radius:50%;background:var(--white);transform:translate(-50%,-50%)}
  .cover-photo{position:absolute;left:0;right:0;top:420px;bottom:0;
    background:linear-gradient(180deg,rgba(215,235,211,0) 0%,#d9c2a6 25%,#a88a6b 60%,#6e5644 100%)}
  .cover-url{position:absolute;left:0;right:0;bottom:30px;text-align:center;color:var(--white);font-size:19px}
</style>
</head>
<body>
<main class="brochure">

  <section class="panel panel--intro">
    <div class="intro-copy">
      <p>Meadowbrook Pet Hospital is a companion animal veterinary Hospital in Tamsworth Vale. We treat Dogs, Cats, Reptiles, Rodents, Birds and other little critters.</p>
      <p>As a companion animal only Hospital, we are dedicated to improving the wellbing of your beloved pets.</p>
      <p>We think they are part of the family and should receive the absolute best possible care.</p>
    </div>
    <div class="intro-photo" role="img" aria-label="Photo of a woman high-fiving a sitting puppy on a sunny path"></div>
    <div class="book-badge">
      <span class="book-badge__icon">
        <svg width="34" height="34" viewBox="0 0 34 34"><path d="M12 24 L22 14 M22 14 L15 14 M22 14 L22 21" stroke="#fff" stroke-width="2.5" fill="none" stroke-linecap="round"/></svg>
      </span>
      <div class="book-badge__title">BOOK ONLINE</div>
      <div class="book-badge__url">www.furlane.example</div>
    </div>
    <div class="intro-phone">
      <svg width="24" height="24" viewBox="0 0 24 24"><path d="M6 3 L9 3 L10.5 8 L8.5 9.5 C9.5 12 12 14.5 14.5 15.5 L16 13.5 L21 15 L21 18 C21 19.5 19.5 21 18 21 C10 20.5 3.5 14 3 6 C3 4.5 4.5 3 6 3 Z" fill="#fff"/></svg>
      61938205
    </div>
  </section>

  <section class="panel panel--contact">
    <div class="contact-photo" role="img" aria-label="Soft-focus photo of a grey cat in a brown tint"></div>
    <div class="hours">
      <span class="hours__icon"></span>
      <span class="hours__day">Mon-Fri</span><span class="hours__time">8:30 AM-6:30 PM</span>
      <span class="hours__day">Sat</span><span class="hours__time">9:00 AM-12 Midday</span>
    </div>
    <div class="contact-name"><span class="contact-name__dot"></span>Meadowbrook<br>Pet Hospital</div>
    <ul class="contact-list">
      <li>
        <svg width="10" height="13" viewBox="0 0 10 13"><path d="M5 0 C2 0 0 2 0 5 C0 8 5 13 5 13 C5 13 10 8 10 5 C10 2 8 0 5 0 Z" fill="#f0883a"/><circle cx="5" cy="5" r="1.8" fill="#6b5646"/></svg>
        14 Marlow Cr, Tamsworth Vale,<br>NSW 2417
      </li>
      <li>
        <svg width="12" height="12" viewBox="0 0 24 24"><path d="M6 3 L9 3 L10.5 8 L8.5 9.5 C9.5 12 12 14.5 14.5 15.5 L16 13.5 L21 15 L21 18 C21 19.5 19.5 21 18 21 C10 20.5 3.5 14 3 6 C3 4.5 4.5 3 6 3 Z" fill="#f0883a"/></svg>
        61938205<br>6193MPET
      </li>
      <li>
        <svg width="12" height="11" viewBox="0 0 12 11"><rect x="3" y="0" width="6" height="4" fill="#f0883a"/><rect x="0" y="4" width="12" height="5" rx="1" fill="#f0883a"/><rect x="3" y="7" width="6" height="4" fill="#f0883a"/></svg>
        61937720
      </li>
      <li>
        <svg width="12" height="9" viewBox="0 0 12 9"><rect x="0" y="0" width="12" height="9" rx="1" fill="#f0883a"/><path d="M0 0 L6 5 L12 0" stroke="#6b5646" fill="none"/></svg>
        contact@furlane.example
      </li>
      <li>
        <svg width="11" height="11" viewBox="0 0 12 12"><circle cx="6" cy="6" r="5" stroke="#f0883a" stroke-width="1.6" fill="none"/><path d="M1 6 H11 M6 1 C3 4 3 8 6 11 C9 8 9 4 6 1" stroke="#f0883a" fill="none"/></svg>
        www.furlane.example
      </li>
      <li>Meadowbrook Pet Hospital</li>
    </ul>
  </section>

  <section class="panel panel--cover">
    <div class="cover-photo" role="img" aria-label="Photo of a woman hugging her shepherd dog"></div>
    <div class="cover-head">
      <span class="cover-brand__dot"></span>
      <div class="cover-brand">Meadowbrook<br>Pet Hospital</div>
      <p class="cover-tagline">Meadowbrook Pet Hospital is a companion<br>Animal Veterinary Hospital in Tamsworth Vale</p>
      <ul class="services">
        <li class="service"><span class="service__icon"></span>Puppy<br>School</li>
        <li class="service"><span class="service__icon"></span>Feline<br>Friendly</li>
        <li class="service"><span class="service__icon"></span>Companion<br>Animal<br>Surgery</li>
        <li class="service"><span class="service__icon"></span>Companion<br>Animal<br>Medicine</li>
      </ul>
    </div>
    <div class="cover-url">www.furlane.example</div>
  </section>

</main>
</body>
</html>
```